Etiketten für alkoholfreien Bio Gin
Zielgruppe
Obsthof Wendlau ist ein innovatives Unternehmen, das sich auf hochwertige Bio- und Wildfruchtspezialitäten in flüssiger Form spezialisiert hat wie z.B. Superfruits sowie konzentrierte Elixire aus Curcuma- oder Ingwerwurzeln. -
Vor Kurzem haben wir mit TAVEL einen alkoholfreien Bio 'Gin' auf den Markt gebracht, der für die Bar-, Gastronomie und Feinkostbranche entwickelt wurde.
Aufgabenstellung
TAVEL ist eine alkoholfreie, bernsteinfarbene Essenz mit 100 % natürlichen Zutaten.
Bio Orangen-, Limetten- und Zitronenschalen sowie frisch gepresste Ingwer und Curcumawurzel werden mit Bio Wacholder nach einer abgestimmten Geheimrezeptur in einer Naturfrucht Essig- und Bio-Honigmischung fermentiert.
So entsteht ein intensives Aromenspiel aus sweet & sour & spicy & bitter Noten.
In den nächsten Wochen wird für TAVEL ein Video produziert. Dort steht TAVEL in einer Höhle und es wird gezeigt, wie die Kraft der Natur direkt in die Flasche fließt. Die Atmosphäre ist mystisch, dunkel, man spürt die unmittelbare Natur aus Wald und Erde. Die Farben sind eher dunkel. Siehe Bild.
Das Etikett soll daher überarbeitet werden und bestenfalls diese Naturgewalten, das Zusammenfließen der Naturrohstoffe darstellen.
Die Flasche bleibt unverändert. Das Etikett darf ganz neu gedacht werden und muss grafisch nicht an die jetzige Version angelehnt sein.
Über ein kreatives Design des Etiketts würden wir uns sehr freuen. Die Bezeichnung Gin soll nicht auf dem Etikett stehen. (Das dürfen nur alkoholische Gins).
Nachtrag:
- Wir wünschen uns, dass das VEL in TAVEL etwas deutlicher hervorgehoben wird, damit die Assoziation zu 'Gin' geweckt wird. Beim Verwenden eines Grüntons, würde 'moosgrün' gut zum Konzept und zur Marke passen.
- Die Schriftarten sind frei wählbar und dürfen gerne moderner wirken.
- Das Etikett umschließt bislang nicht die gesamte Flasche. Dh. zzgl. 25 mm sind möglich, was der Vorderseite auch grafisch mehr Platz gibt.
Auch die Höhe ist nicht definiert. Bis zu 110 mm Gesamthöhe ist machbar.
- Auf der Vorderseite kann auf den Text 'Aus frischen ...Honig' verzichtet werden.
- Bitte gerne den exklusiven Charakter herausstellen. Auch Prägungen und eine hochwertige Ausführung sind gut möglich.

```html
<!DOCTYPE html>
<html lang="de">
<head>
<meta charset="utf-8">
<title>TAVEL – Well Spirit Drink Etikett</title>
<link rel="stylesheet" href="https://fonts.googleapis.com/css2?family=Antonio:wght@300&family=Cormorant+Garamond:ital,wght@0,600;1,500&family=Oswald:wght@400;500&display=swap">
<style>
  :root {
    --stage: #0a0908;
    --label-top: #262a22;
    --label-bottom: #151612;
    --gold: #e2c98f;
    --gold-soft: #cdb27a;
    --gold-dim: rgba(214, 184, 128, 0.45);
    --ivory: #efe6d2;
  }
  * { margin: 0; padding: 0; box-sizing: border-box; }
  html, body {
    width: 1200px; height: 690px; overflow: hidden;
    background: var(--stage);
  }
  .canvas {
    position: relative; width: 1200px; height: 690px;
    display: flex; align-items: center; justify-content: center;
  }
  .label {
    position: relative; width: 560px; height: 640px;
    background: radial-gradient(ellipse at 50% 40%, var(--label-top) 0%, var(--label-bottom) 75%);
    overflow: hidden;
    color: var(--gold);
  }
  .burst {
    position: absolute; left: 0; top: 60px; width: 560px; height: 520px;
  }
  .tagline {
    position: absolute; top: 96px; width: 100%; text-align: center;
    font-family: "Cormorant Garamond", serif; font-weight: 600;
    font-size: 17px; letter-spacing: 1.5px; color: var(--gold-soft);
  }
  .wordmark {
    position: absolute; top: 140px; left: 0; width: 100%; height: 210px;
    display: flex; align-items: center; justify-content: center;
    font-family: "Antonio", sans-serif; font-weight: 300;
    font-size: 210px; line-height: 1; letter-spacing: 6px;
    color: var(--gold);
  }
  .strength {
    position: absolute; top: 364px; width: 100%; text-align: center;
    font-family: "Oswald", sans-serif; font-weight: 500;
    font-size: 15px; letter-spacing: 3px; color: var(--gold);
  }
  .free {
    position: absolute; top: 396px; width: 100%; text-align: center;
    font-family: "Cormorant Garamond", serif; font-weight: 600;
    font-size: 20px; letter-spacing: 1px; color: var(--gold-soft);
  }
  .edition {
    position: absolute; top: 420px; width: 100%; text-align: center;
    font-family: "Cormorant Garamond", serif; font-style: italic; font-weight: 500;
    font-size: 30px; letter-spacing: 1px; color: var(--gold-soft);
  }
  .variety {
    position: absolute; bottom: 58px; width: 100%;
    display: flex; align-items: center; justify-content: center; gap: 12px;
    font-family: "Oswald", sans-serif; font-weight: 400; font-size: 30px;
    letter-spacing: 2px; color: var(--ivory);
  }
  .variety .dot {
    width: 7px; height: 7px; background: var(--ivory); transform: rotate(45deg);
  }
</style>
</head>
<body>
<main class="canvas">
  <section class="label">
    <svg class="burst" viewBox="0 0 560 520" role="img" aria-label="Soft golden glow with a thin ring behind the name">
      <defs>
        <radialGradient id="burstGlow" cx="50%" cy="48%" r="50%">
          <stop offset="0%" stop-color="#b89a62" stop-opacity="0.2"/>
          <stop offset="60%" stop-color="#8c7448" stop-opacity="0.07"/>
          <stop offset="100%" stop-color="#8c7448" stop-opacity="0"/>
        </radialGradient>
      </defs>
      <rect width="560" height="520" fill="url(#burstGlow)"/>
      <circle cx="280" cy="250" r="215" fill="none" stroke="var(--gold-dim)" stroke-width="1"/>
    </svg>

    <p class="tagline">WELL SPIRIT DRINK</p>

    <h1 class="wordmark">TAVEL</h1>

    <p class="strength">NULL ALC. 0 ‰</p>
    <p class="free">FREE ‰</p>
    <p class="edition">exclusive edition</p>

    <p class="variety"><span class="dot"></span>BIO SHRUB<span class="dot"></span></p>
  </section>
</main>
</body>
</html>
```